Business Card Design Project

We need a simple business card design that uses our current logo.
We need to have the current logo put into a high res format.
We need to have 1 card made with contact information.
We will supply the information for the 4 employees.
Industry/Entity Type
Business
Requirements
Must have
- The contact information is as follows:
Mark Dellweather
Producer/CEO
c. 949-555-0147
f. 650-555-0193
markd@lanternbay.example
Al Vostrand, CFO
c. 949-555-0162
f. 650-555-0193
alv@lanternbay.example
Peter Malvane, PR
c. 267-555-0128
f. 650-555-0193
pmalvane@lanternbay.example
Tim Garrowby, Producer
c. 949-555-0184
f. 650-555-0193
timg@lanternbay.example
The address for all cards is:
318 W Calle Norvento #2715, San Clemente, CA 92681

```html
<!DOCTYPE html>
<html lang="en">
<head>
<meta charset="utf-8">
<title>Lantern Bay Media – Business Card</title>
<link href="https://fonts.googleapis.com/css2?family=Jost:wght@400;500;700&display=swap" rel="stylesheet">
<style>
  :root {
    --page: #ffffff;
    --card-dark: #000000;
    --card-glow: #4a4a4a;
    --accent: #5cc3ee;
    --contact: #c4c4c4;
    --address: #a8a8a8;
  }
  html, body {
    margin: 0;
    padding: 0;
    width: 1200px;
    height: 960px;
    overflow: hidden;
    background: var(--page);
  }
  .canvas {
    position: relative;
    width: 1200px;
    height: 960px;
  }
  .business-card {
    position: absolute;
    left: 200px;
    top: 230px;
    width: 803px;
    height: 460px;
    overflow: hidden;
    background: radial-gradient(ellipse 520px 420px at 560px 300px, var(--card-glow) 0%, #262626 45%, #0d0d0d 75%, var(--card-dark) 100%);
    font-family: "Jost", "Futura", sans-serif;
  }
  .brand-texture {
    position: absolute;
    left: 0;
    top: 0;
    width: 430px;
    height: 460px;
  }
  .contact-block {
    position: absolute;
    right: 43px;
    top: 76px;
    text-align: right;
  }
  .person-name {
    margin: 0;
    font-size: 23px;
    font-weight: 500;
    letter-spacing: 2px;
    color: var(--accent);
    line-height: 30px;
  }
  .person-title {
    margin: 0 0 8px;
    font-size: 20px;
    font-weight: 500;
    letter-spacing: 1px;
    color: var(--accent);
    line-height: 26px;
  }
  .contact-line {
    margin: 0;
    font-size: 20px;
    font-weight: 400;
    letter-spacing: 3px;
    color: var(--contact);
    line-height: 27px;
  }
  .company-name {
    position: absolute;
    right: 40px;
    top: 355px;
    margin: 0;
    font-size: 36px;
    font-weight: 700;
    color: var(--accent);
    line-height: 44px;
    letter-spacing: 0.5px;
  }
  .company-address {
    position: absolute;
    right: 35px;
    top: 412px;
    margin: 0;
    font-size: 20px;
    font-weight: 400;
    color: var(--address);
    letter-spacing: 0.5px;
    line-height: 26px;
  }
</style>
</head>
<body>
<div class="canvas">
  <section class="business-card">
    <svg class="brand-texture" viewBox="0 0 430 460" role="img" aria-label="Faint repeated vertical company name texture">
      <defs>
        <linearGradient id="column-fade" x1="0" y1="0" x2="0" y2="1">
          <stop offset="0" stop-color="#2a2a2a" stop-opacity="0.35"/>
          <stop offset="1" stop-color="#3a3a3a" stop-opacity="0.6"/>
        </linearGradient>
      </defs>
      <rect x="40" y="50" width="42" height="410" fill="url(#column-fade)"/>
      <rect x="122" y="0" width="42" height="460" fill="url(#column-fade)"/>
      <rect x="238" y="50" width="42" height="410" fill="url(#column-fade)"/>
      <rect x="320" y="0" width="42" height="460" fill="url(#column-fade)"/>
    </svg>

    <div class="contact-block">
      <p class="person-name">MARK DELLWEATHER</p>
      <p class="person-title">Producer/CEO</p>
      <p class="contact-line">c. 949-555-0147</p>
      <p class="contact-line">f. 650-555-0193</p>
      <p class="contact-line">markd@lanternbay.example</p>
    </div>

    <p class="company-name">LANTERN BAY MEDIA</p>
    <p class="company-address">318 W Calle Norvento #2715, San Clemente, CA 92681</p>
  </section>
</div>
</body>
</html>
```